Corvane Project Services - Flyer

Project Breif:
I need a single page A4 Capability Statement, which will be used to market our services to prospective clients, both in print and via email PDF.
It needs to look professional and should incorporate the elements I have uploaded into files, these include:
Capability Statement Text
Corvane Services Company Logo
Additional Logo’s (Tools We Use)
Glimmer Bay Pics can be cut into the page
I have included examples of capability statements as a guide to what i am looking for.
Regards
Derek
Engineering Consulting

```html
<!DOCTYPE html>
<html lang="en">
<head>
<meta charset="utf-8">
<title>Corvane Project Services – Capability Statement</title>
<link href="https://fonts.googleapis.com/css2?family=Lato:wght@400;700;900&family=Michroma&display=swap" rel="stylesheet">
<style>
  :root{
    --navy:#0b3a8c;
    --blue:#1f5fbf;
    --sky:#5bb8ea;
    --sky-light:#a9d9f3;
    --sky-dark:#3d9fdc;
    --ink:#1a1a1a;
    --white:#ffffff;
    --grey:#eef2f6;
    --contact:#b9d7ee;
  }
  html,body{margin:0;padding:0;overflow:hidden;background:#fff}
  .flyer{position:relative;width:800px;height:1200px;overflow:hidden;background:var(--white);font-family:"Lato",sans-serif;color:var(--ink)}
  .hero-photo{position:absolute;left:0;top:0;width:800px;height:340px;
    background:linear-gradient(90deg,#ffffff 0%,#f2f5f8 35%,#dfe6ee 60%,#cfd9e3 100%)}
  .hero-fade{position:absolute;left:0;top:260px;width:800px;height:90px;background:linear-gradient(180deg,rgba(255,255,255,0),#fff)}
  .brand{position:absolute;left:40px;top:90px;width:330px}
  .brand-mark{width:70px;height:70px;border-radius:50%;background:var(--blue);margin:0 0 70px 130px}
  .brand-name{font-family:"Michroma",sans-serif;font-size:25px;color:var(--ink);letter-spacing:1px;border-bottom:2px solid var(--ink);padding-bottom:2px;white-space:nowrap}
  .brand-sub{font-family:"Michroma",sans-serif;font-size:17px;color:var(--blue);letter-spacing:9px;margin:4px 0 0 60px}
  .intro{position:absolute;left:38px;top:362px;width:720px;margin:0;padding:0;list-style:none;font-size:14.5px;line-height:18px}
  .intro li{position:relative;padding-left:20px;margin-bottom:11px}
  .intro li::before{content:"";position:absolute;left:2px;top:5px;width:8px;height:8px;border-radius:50%;background:#555}
  .pill{position:absolute;left:270px;width:260px;height:34px;border-radius:7px;background:var(--navy);color:#fff;font-size:17px;text-align:center;line-height:34px;letter-spacing:.3px}
  .pill-core{top:571px}
  .pill-cost{top:836px}
  .services{position:absolute;left:0;top:619px;width:800px;height:205px;background:linear-gradient(90deg,var(--sky-light),var(--sky) 50%,var(--sky-light))}
  .services-head{height:38px;background:var(--sky-dark);opacity:.85}
  .col{position:absolute;top:0;width:380px}
  .col-left{left:62px}
  .col-right{left:460px}
  .col h3{margin:0;height:38px;line-height:38px;font-size:15px;font-weight:400;color:#fff}
  .col ul{list-style:none;margin:8px 0 0;padding:0;font-size:14.5px;line-height:19.5px;color:var(--navy)}
  .col li{padding-left:26px;position:relative}
  .col li::before{content:"";position:absolute;left:2px;top:4px;width:5px;height:9px;border-right:2px solid var(--navy);border-bottom:2px solid var(--navy);transform:rotate(40deg)}
  .tools{position:absolute;left:0;top:885px;width:800px;height:150px}
  .tool{position:absolute;width:180px;text-align:center;color:var(--blue);font-size:14.5px;line-height:20px}
  .tool svg{display:block;margin:0 auto 12px}
  .contact{position:absolute;left:0;top:1064px;width:800px;height:64px;background:var(--contact)}
  .contact-person{position:absolute;left:36px;top:8px;font-size:12px;line-height:14px}
  .contact-person strong{display:block;font-size:16px;font-weight:400}
  .contact-person small{font-size:10px}
  .contact-line{position:absolute;left:205px;top:22px;font-size:14px;color:var(--navy);display:flex;align-items:center;gap:10px}
  .contact-line .sep{width:1px;height:16px;background:var(--navy)}
  .contact-line svg{vertical-align:middle}
  .partners{position:absolute;left:0;top:1128px;width:800px;height:72px;display:flex;justify-content:space-around;align-items:center;padding:0 20px;box-sizing:border-box}
  .partner{font-size:13px;font-weight:700;color:var(--navy);display:flex;align-items:center;gap:6px}
  .partner i{display:inline-block;width:12px;height:12px;background:var(--navy)}
</style>
</head>
<body>
<div class="flyer">
  <div class="hero-photo" role="img" aria-label="Stock photograph of colleagues reviewing printed charts and documents at a desk, framed by a silver curved swoosh"></div>
  <div class="hero-fade"></div>

  <div class="brand">
    <div class="brand-mark"></div>
    <div class="brand-name">CORVANE PROJECT</div>
    <div class="brand-sub">SERVICES</div>
  </div>

  <ul class="intro">
    <li>Corvane Project Services Ltd. is a leading project control consultancy based in Co Cork Ireland</li>
    <li>For over 20 years we have been helping our clients to deliver complex projects and programs throughout mainland Europe.</li>
    <li>We are passionate about empower organisations to achieve their objectives, on time and on budget.</li>
    <li>We are continually innovating, evolving and learning, utilize the latest industry tools and techniques to deliver real value to our clients.</li>
    <li>Our goal is to make successful project delivery more achievable and repeatable.</li>
  </ul>

  <div class="pill pill-core">CORE SERVICES</div>

  <section class="services">
    <div class="services-head"></div>
    <div class="col col-left">
      <h3>Planning and Scheduling</h3>
      <ul>
        <li>Tender Planning</li>
        <li>Interactive Planning / Pull Planning</li>
        <li>EPCMV Planning &amp; Scheduling</li>
        <li>Schedule Earned Value Management</li>
        <li>Independent Schedule Quality Assessment</li>
        <li>Schedule Risk Analysis (Monte Carlo)</li>
        <li>Training</li>
      </ul>
    </div>
    <div class="col col-right">
      <h3>Management of Risk</h3>
      <ul>
        <li>Risk Management Policies &amp; Procedures</li>
        <li>Risk Management Strategy</li>
        <li>Risk Registers</li>
        <li>Risk Improvement Planning</li>
        <li>Risk Response and Communication</li>
        <li>Risk Management Training</li>
      </ul>
    </div>
  </section>

  <div class="pill pill-cost">COST CONTROL</div>

  <section class="tools">
    <div class="tool" style="left:33px">
      <svg width="100" height="100" viewBox="0 0 100 100"><circle cx="50" cy="50" r="47" fill="var(--sky)" stroke="var(--sky-light)" stroke-width="4"/><rect x="33" y="28" width="30" height="42" rx="3" fill="none" stroke="#fff" stroke-width="3"/><rect x="38" y="33" width="20" height="8" fill="#fff"/><g fill="#fff"><rect x="38" y="46" width="5" height="5"/><rect x="46" y="46" width="5" height="5"/><rect x="54" y="46" width="5" height="5"/><rect x="38" y="55" width="5" height="5"/><rect x="46" y="55" width="5" height="5"/><rect x="54" y="55" width="5" height="10"/></g></svg>
      Estimating &amp;<br>Forecasting
    </div>
    <div class="tool" style="left:215px">
      <svg width="100" height="100" viewBox="0 0 100 100"><circle cx="50" cy="50" r="47" fill="var(--sky)" stroke="var(--sky-light)" stroke-width="4"/><circle cx="45" cy="44" r="15" fill="none" stroke="#fff" stroke-width="3"/><line x1="56" y1="55" x2="68" y2="67" stroke="#fff" stroke-width="5" stroke-linecap="round"/><text x="45" y="50" font-size="17" text-anchor="middle" fill="#fff" font-family="Lato,sans-serif" font-weight="700">$</text></svg>
      Earned Value<br>Analysis
    </div>
    <div class="tool" style="left:397px">
      <svg width="100" height="100" viewBox="0 0 100 100"><circle cx="50" cy="50" r="47" fill="var(--sky)" stroke="var(--sky-light)" stroke-width="4"/><g fill="#fff"><rect x="30" y="58" width="6" height="10"/><rect x="39" y="52" width="6" height="16"/><rect x="48" y="47" width="6" height="21"/><rect x="57" y="42" width="6" height="26"/></g><polyline points="28,52 40,42 50,46 66,30" fill="none" stroke="#fff" stroke-width="3"/><polygon points="70,26 60,28 68,36" fill="#fff"/></svg>
      Progress<br>Reporting
    </div>
    <div class="tool" style="left:579px">
      <svg width="100" height="100" viewBox="0 0 100 100"><circle cx="50" cy="50" r="47" fill="var(--sky)" stroke="var(--sky-light)" stroke-width="4"/><polygon points="55,28 74,64 36,64" fill="none" stroke="#fff" stroke-width="3" stroke-linejoin="round"/><line x1="58" y1="42" x2="58" y2="53" stroke="#fff" stroke-width="3"/><circle cx="58" cy="58" r="1.8" fill="#fff"/><circle cx="42" cy="58" r="10" fill="var(--sky)" stroke="#fff" stroke-width="3"/><text x="42" y="63" font-size="13" text-anchor="middle" fill="#fff" font-family="Lato,sans-serif" font-weight="700">$</text></svg>
      Cost Risk<br>Analysis
    </div>
  </section>

  <section class="contact">
    <div class="contact-person">Contact:<strong>Derek Hallorin</strong><small>(Managing Director)</small></div>
    <div class="contact-line">
      <svg width="16" height="16" viewBox="0 0 16 16"><path d="M3 1l3 3-2 2c1 2 3 4 5 5l2-2 3 3-2 3C6 15 1 10 1 3z" fill="var(--navy)"/></svg>
      <span>+353 (0)870001234</span><span class="sep"></span>
      <svg width="16" height="12" viewBox="0 0 16 12"><rect x="1" y="1" width="14" height="10" fill="none" stroke="var(--navy)" stroke-width="1.5"/><polyline points="1,1 8,7 15,1" fill="none" stroke="var(--navy)" stroke-width="1.5"/></svg>
      <span>info@corvaneservices.ie</span><span class="sep"></span>
      <svg width="16" height="16" viewBox="0 0 16 16"><circle cx="8" cy="8" r="7" fill="none" stroke="var(--navy)" stroke-width="1.5"/><ellipse cx="8" cy="8" rx="3" ry="7" fill="none" stroke="var(--navy)" stroke-width="1.2"/><line x1="1" y1="8" x2="15" y2="8" stroke="var(--navy)" stroke-width="1.2"/></svg>
      <span>www.corvaneservices.ie</span>
    </div>
  </section>

  <section class="partners">
    <span class="partner">Veltrane Planner</span>
    <span class="partner"><i></i>Plansheet</span>
    <span class="partner">Orvik Scheduler</span>
    <span class="partner">Markpost Pro</span>
    <span class="partner">Quillon | Benchline</span>
    <span class="partner">RiskPath</span>
  </section>
</div>
</body>
</html>
```